Web Button design and production

I need remote control like buttons (or your own design of buttons if I like it)
3x4 text buttons (normal, pressed, disabled)
3x1 empty button (normal, pressed, disabled)
3x6 buttons with glyph (normal, pressed, disabled)
3x288 with 24h time "00:00", "00:05", "00:10" (normal, pressed, disabled)
4 LED (red, green, orange, black)
I will upload the background image as soon as possible (black plastic)
See attached images
Q: Do the buttons have to be gray/black?
A: It should look like a high end remote control. It could be brushed aluminum as well, or something you come up with. But I guess black or dark grey would be best. The background will be picsharbor 40561739, but it's not available yet.
Q: Do I have to provide all buttons for the contest?
A: No! I only need one button (3 states) and a LED to decide. Only the winner will do the whole job.
Q: Is the Designer who wins the contest expected to complete all the extra buttons?
A: Yes, please.
Plastic

```html
<!DOCTYPE html>
<html lang="en">
<head>
<meta charset="utf-8">
<title>Remote Control Buttons — Plastic</title>
<link href="https://fonts.googleapis.com/css2?family=Lobster&family=Anonymous+Pro&display=swap" rel="stylesheet">
<style>
  :root {
    --bg-center: #363636;
    --bg-edge: #1f1f1f;
    --label: #f4f4f4;
    --btn-top: #363636;
    --btn-bottom: #2a2a2a;
    --btn-border: #1a1a1a;
    --btn-highlight: rgba(255,255,255,0.07);
    --pressed-fill: #1e1e1e;
    --disabled-fill: #2e2e2e;
    --text-light: #e6e6e6;
    --text-disabled: #1e1e1e;
    --led-ring-top: #f2f2f2;
    --led-ring-bottom: #8a8a8a;
  }
  html, body {
    margin: 0;
    padding: 0;
    width: 1200px;
    height: 1200px;
    overflow: hidden;
  }
  body {
    background: radial-gradient(ellipse at 50% 45%, var(--bg-center) 0%, #2b2b2b 55%, var(--bg-edge) 100%);
    position: relative;
  }
  .led-row { position: absolute; top: 194px; left: 386px; display: flex; gap: 28px; }
  .led {
    width: 92px; height: 92px; border-radius: 50%;
    background: linear-gradient(180deg, var(--led-ring-top), var(--led-ring-bottom));
    box-shadow: 0 4px 8px rgba(0,0,0,0.6);
    display: flex; align-items: center; justify-content: center;
  }
  .led__lamp {
    width: 70px; height: 70px; border-radius: 50%;
    box-shadow: inset 0 2px 6px rgba(0,0,0,0.5);
  }
  .led--red .led__lamp { background: radial-gradient(circle at 50% 35%, #ff9a9a 0%, #e0242a 35%, #8a0b10 100%); }
  .led--green .led__lamp { background: radial-gradient(circle at 50% 35%, #c8ffb8 0%, #3cc41c 38%, #1a6e08 100%); }
  .led--orange .led__lamp { background: radial-gradient(circle at 50% 35%, #ffe38a 0%, #ffa200 38%, #c06000 100%); }
  .led--off .led__lamp { background: radial-gradient(circle at 50% 35%, #ffffff 0%, #dcdcdc 40%, #9a9a9a 100%); }

  .state-label {
    position: absolute; top: 360px; width: 240px; margin-left: -120px;
    text-align: center; font-family: "Lobster", cursive; font-size: 35px;
    color: var(--label); text-shadow: 0 2px 3px rgba(0,0,0,0.6);
  }
  .state-label--normal { left: 360px; }
  .state-label--pressed { left: 600px; }
  .state-label--disabled { left: 840px; }

  .btn {
    position: absolute; width: 192px; height: 120px; box-sizing: border-box;
    border-radius: 7px; border: 2px solid var(--btn-border);
    display: flex; align-items: center; justify-content: center;
    font-family: "Anonymous Pro", monospace; font-size: 32px; letter-spacing: 1px;
  }
  .btn--normal {
    left: 264px;
    background: linear-gradient(180deg, var(--btn-top), var(--btn-bottom));
    box-shadow: inset 0 2px 0 var(--btn-highlight), 0 3px 6px rgba(0,0,0,0.55);
    color: var(--text-light); text-shadow: 0 -1px 1px rgba(0,0,0,0.7);
  }
  .btn--pressed {
    left: 504px;
    background: var(--pressed-fill);
    border-color: #141414;
    box-shadow: inset 0 3px 8px rgba(0,0,0,0.8), 0 2px 0 rgba(255,255,255,0.05);
    color: var(--text-light);
  }
  .btn--disabled {
    left: 744px;
    background: var(--disabled-fill);
    border-color: #232323;
    box-shadow: 0 2px 4px rgba(0,0,0,0.35);
    color: var(--text-disabled); text-shadow: 0 1px 0 rgba(255,255,255,0.08);
  }
  .row--glyph { top: 454px; }
  .row--time { top: 670px; }
  .row--text { top: 886px; }
  .glyph { width: 56px; height: 34px; }
  .glyph path { fill: #dcdcdc; }
  .btn--disabled .glyph path { fill: #1a1a1a; }
</style>
</head>
<body>
  <div class="led-row">
    <div class="led led--red"><div class="led__lamp"></div></div>
    <div class="led led--green"><div class="led__lamp"></div></div>
    <div class="led led--orange"><div class="led__lamp"></div></div>
    <div class="led led--off"><div class="led__lamp"></div></div>
  </div>

  <div class="state-label state-label--normal">Normal</div>
  <div class="state-label state-label--pressed">Pressed</div>
  <div class="state-label state-label--disabled">Disabled</div>

  <div class="btn btn--normal row--glyph"><svg class="glyph" viewBox="0 0 56 34"><path d="M2 2 L27 17 L2 32 Z"/><path d="M29 2 L54 17 L29 32 Z"/></svg></div>
  <div class="btn btn--pressed row--glyph"><svg class="glyph" viewBox="0 0 56 34"><path d="M2 2 L27 17 L2 32 Z"/><path d="M29 2 L54 17 L29 32 Z"/></svg></div>
  <div class="btn btn--disabled row--glyph"><svg class="glyph" viewBox="0 0 56 34"><path d="M2 2 L27 17 L2 32 Z"/><path d="M29 2 L54 17 L29 32 Z"/></svg></div>

  <div class="btn btn--normal row--time">18.50</div>
  <div class="btn btn--pressed row--time">18.50</div>
  <div class="btn btn--disabled row--time">18.50</div>

  <div class="btn btn--normal row--text">Login</div>
  <div class="btn btn--pressed row--text">Login</div>
  <div class="btn btn--disabled row--text">Login</div>
</body>
</html>
```